Hair Extension Packaging

Update 2/16 - please keep submissions coming, I have no front runners yet. Thanks.

I need some new packaging designed for hair extensions. I have enclose pictures of what other companies packaging looks like and a few pictures of some inspiration. I am looking for a packaging that will appeal to a 20's-30's year old demographic and I like things along the lines of glamor/lace/vintage/boudoir/damask inspired. I am going to leave colors up to your creativity for the sample artwork and ask for changes if needed. Id like the design to be a standout but not loud.

The working name for this hair is "Vexa"
Additional Text that I would like on the packaging "100% Premium Virgin Remy Human Hair"

Please keep in mind that the background of the packaging will have many different colors laying over it so be mindful of what the color you chose can effect the hair color in the packaging - no red or orange which can make the hair appear very warm and clash with ashy colors.

Working dimensions for the sample are 22" long, 3" wide.

****Once I decide on the front of the packaging I will also need the back designed which will consist of similar design as the front but with hair care instructions printed on it.***** This finished product must include front and back artwork, open Photoshop files, and additional bleed room for printing. I don't want to waste anyone's time so once I get a front design I like I will work with that artist to create the back.

Please message me with any questions.
Updates

Project Deadline Extended
Reason: Finalizing final choices. Thanks for your submissions!

Target Market(s)

Women in there 20"s - 30's. High fashion, luxurious, glamour

Industry/Entity Type

Hair

Font styles to use
Serif
Script

Requirements
Must have
• Id love the product name to be in script and then mixed with regular font (see the makeup logo example I enclosed)
Should not have
• Should not be masculine. Forget the blue and green colors

```html
<!DOCTYPE html>
<html lang="en">
<head>
<meta charset="utf-8">
<title>Vexa Hair Extension Packaging</title>
<link rel="stylesheet" href="https://fonts.googleapis.com/css2?family=Questrial&display=swap">
<style>
  :root {
    --canvas: #ffffff;
    --card: #ffffff;
    --header: #231f20;
    --body: #383536;
    --type: #ffffff;
    --accent-white: #ffffff;
    --accent-pink: #e6007e;
    --accent-gold: #f9ad1b;
    --accent-lime: #a8cb55;
    --band-white: #a3a3a3;
    --band-pink: #8f1e52;
    --band-gold: #8e6c22;
    --band-lime: #5b7b34;
  }
  * { margin: 0; padding: 0; box-sizing: border-box; }
  html, body { width: 1200px; height: 1000px; overflow: hidden; background: var(--canvas); }
  body { position: relative; font-family: "Questrial", "Century Gothic", sans-serif; color: var(--type); }

  .package {
    position: absolute;
    top: 84px;
    width: 246px;
    height: 822px;
    background: var(--card);
    box-shadow: 4px 3px 5px rgba(0,0,0,0.35);
  }
  .package:nth-child(1) { left: 50px; }
  .package:nth-child(2) { left: 332px; }
  .package:nth-child(3) { left: 614px; }
  .package:nth-child(4) { left: 896px; }

  .package-body {
    position: absolute;
    left: 15px;
    top: 13px;
    width: 216px;
    bottom: 0;
    background: var(--body);
  }
  .package-header {
    position: absolute;
    left: 0; top: 0;
    width: 216px;
    height: 253px;
    background: var(--header);
    box-shadow: 0 4px 7px rgba(0,0,0,0.45);
    text-align: center;
  }
  .category {
    position: absolute;
    top: 45px; left: 0; right: 0;
    font-size: 21px;
    letter-spacing: 0.2px;
  }
  .product-name {
    position: absolute;
    top: 78px; left: 0; right: 0;
    font-size: 58px;
    line-height: 1;
    letter-spacing: -1px;
    color: var(--accent);
  }
  .tagline {
    position: absolute;
    top: 135px; left: 0; right: 0;
    font-size: 14px;
  }
  .claim-band {
    position: absolute;
    top: 185px; left: 0;
    width: 216px; height: 35px;
    background: linear-gradient(90deg, var(--band) 0%, var(--band) 40%, rgba(35,31,32,0) 100%);
    font-size: 9px;
    line-height: 10px;
    padding-top: 7px;
  }
  .package--white { --accent: var(--accent-white); }
  .package--white .claim-band { background: linear-gradient(90deg, rgba(35,31,32,0) 5%, var(--band-white) 45%, var(--band-white) 100%); }
  .package--pink { --accent: var(--accent-pink); --band: var(--band-pink); }
  .package--gold { --accent: var(--accent-gold); --band: var(--band-gold); }
  .package--lime { --accent: var(--accent-lime); --band: var(--band-lime); }
</style>
</head>
<body>
  <div class="package package--white">
    <div class="package-body">
      <div class="package-header">
        <p class="category">HAIR EXTENSION</p>
        <h1 class="product-name">VEXA</h1>
        <p class="tagline">Be bold and beautiful</p>
        <p class="claim-band">100% Premium Virgin Remy<br>Human Hair</p>
      </div>
    </div>
  </div>
  <div class="package package--pink">
    <div class="package-body">
      <div class="package-header">
        <p class="category">HAIR EXTENSION</p>
        <h1 class="product-name">VEXA</h1>
        <p class="tagline">Be bold and beautiful</p>
        <p class="claim-band">100% Premium Virgin Remy<br>Human Hair</p>
      </div>
    </div>
  </div>
  <div class="package package--gold">
    <div class="package-body">
      <div class="package-header">
        <p class="category">HAIR EXTENSION</p>
        <h1 class="product-name">VEXA</h1>
        <p class="tagline">Be bold and beautiful</p>
        <p class="claim-band">100% Premium Virgin Remy<br>Human Hair</p>
      </div>
    </div>
  </div>
  <div class="package package--lime">
    <div class="package-body">
      <div class="package-header">
        <p class="category">HAIR EXTENSION</p>
        <h1 class="product-name">VEXA</h1>
        <p class="tagline">Be bold and beautiful</p>
        <p class="claim-band">100% Premium Virgin Remy<br>Human Hair</p>
      </div>
    </div>
  </div>
</body>
</html>
```